Your conflict - our mediation - joint conflict SOLUTION

With this flyer I am looking for conflict parties who are ready to tackle and resolve their conflict with a prospective mediator. The mediation is free because I am doing it as part of my diploma thesis. Time frame approx. 4 sessions of 2.5 hours each. The wishes and needs of both parties are listened to and “picked out”. In an open, constructive, appreciative framework, solutions are developed and negotiated together.

Target Market(s)

everyone who is ready to deal with himself and his counterpart and everyone who wants to work out a solution with the respect, openness and support of a mediator.

Requirements
Must have
• - "For my diploma thesis I am looking for conflicting parties who are willing to resolve their conflict with a mediator"
- Time frame: 4 x 2.5 hours feasible in Solothurn, Bern, Brugg
- Free of charge
- my coordinates - see business card
- more information at www.talweidenhof.ch
Nice to have
• the card should be based on the style of my homepage www.talweidenhof.ch and my business card

```html
<!DOCTYPE html>
<html lang="de">
<head>
<meta charset="utf-8">
<title>Konflikt Streit Blockade – Mediation</title>
<link rel="stylesheet" href="https://fonts.googleapis.com/css2?family=Libre+Baskerville:wght@700&family=Montserrat:wght@400;500;700;800&display=swap">
<style>
  :root {
    --purple: #4d2f66;
    --purple-deep: #3e2454;
    --purple-text: #4a2a6b;
    --gold: #b8904a;
    --grey-band: #d9d9d9;
    --white: #ffffff;
    --ink: #222222;
    --page-bg: #b4b4b4;
  }
  * { margin: 0; padding: 0; box-sizing: border-box; }
  html, body { width: 800px; height: 1200px; overflow: hidden; background: var(--page-bg); }
  .flyer {
    position: relative; width: 800px; height: 1200px;
    background: var(--white); overflow: hidden;
    font-family: "Montserrat", Arial, sans-serif; color: var(--ink);
  }
  .hero { position: absolute; left: 0; top: 92px; width: 800px; height: 493px; background: var(--purple); }
  .hero-portrait {
    position: absolute; left: 0; top: 20px; width: 316px; height: 565px;
    background: linear-gradient(180deg, #c9b6a6 0%, #efe9e4 35%, #2a2a34 70%, #1f1f28 100%);
    border-radius: 140px 140px 0 0;
  }
  .headline {
    position: absolute; left: 376px; top: 142px;
    font-family: "Libre Baskerville", Georgia, serif; font-weight: 700;
    font-size: 54px; line-height: 58px; letter-spacing: 1px; text-transform: uppercase;
  }
  .headline .gold { color: var(--gold); display: block; }
  .headline .light { color: var(--white); display: block; }
  .headline-rule { position: absolute; left: 376px; top: 347px; }
  .contacts-list {
    position: absolute; left: 376px; top: 414px; width: 370px;
    color: #e8e0ef; font-size: 14.5px; line-height: 17.5px;
  }
  .stuck-question {
    position: absolute; left: 60px; top: 608px;
    font-weight: 700; font-size: 19px; letter-spacing: .3px;
  }
  .grey-band { position: absolute; left: 0; top: 649px; width: 800px; height: 210px; background: var(--grey-band); }
  .mediation-title {
    position: absolute; left: 60px; top: 674px;
    font-family: "Libre Baskerville", Georgia, serif; font-weight: 700;
    font-size: 33px; color: var(--purple-text); letter-spacing: .5px;
  }
  .mediation-text { position: absolute; left: 60px; top: 726px; width: 400px; font-size: 13.3px; line-height: 16.5px; }
  .mediation-text p + p { margin-top: 16px; }
  .illustration {
    position: absolute; left: 498px; top: 602px; width: 222px; height: 306px;
    border: 1.5px solid #333;
    background: linear-gradient(180deg, #ffffff 0%, #eceaf6 55%, #e9ddd4 100%);
  }
  .thesis-call { position: absolute; left: 60px; top: 878px; width: 420px; font-size: 15.5px; line-height: 20px; }
  .time-frame { position: absolute; left: 60px; top: 962px; font-size: 18.5px; line-height: 24px; }
  .time-frame strong { display: block; font-weight: 800; color: var(--purple-text); font-size: 21px; }
  .free-label {
    position: absolute; left: 60px; top: 1066px;
    font-weight: 800; font-size: 32px; color: var(--purple-text); letter-spacing: .6px;
  }
  .brand-mark { position: absolute; left: 510px; top: 1000px; display: flex; align-items: center; gap: 12px; }
  .brand-mark .dot { width: 34px; height: 34px; border-radius: 50%; background: var(--gold); }
  .brand-mark .name { font-family: "Montserrat", Arial, sans-serif; font-weight: 500; font-size: 28px; color: var(--gold); }
  .footer { position: absolute; left: 0; top: 1127px; width: 800px; height: 73px; }
  .footer-url {
    position: absolute; left: 62px; top: 1145px;
    font-size: 24px; letter-spacing: 1.2px; color: var(--white); font-weight: 500;
  }
</style>
</head>
<body>
<main class="flyer">
  <div class="hero"></div>
  <div class="hero-portrait" role="img" aria-label="Portrait photo of the mediator holding a tablet"></div>

  <h1 class="headline">
    <span class="gold">Konflikt</span>
    <span class="gold">Streit</span>
    <span class="light">Blockade</span>
  </h1>
  <svg class="headline-rule" width="180" height="14" viewBox="0 0 180 14" aria-hidden="true">
    <line x1="0" y1="7" x2="180" y2="7" stroke="#ffffff" stroke-width="1.5"/>
    <rect x="14" y="3" width="46" height="8" rx="4" fill="#ffffff"/>
  </svg>
  <p class="contacts-list">mit Ihrer Ehefrau … Ihrem Vertragspartner … Ihrer Nachbarin … Ihrem Mieter … Ihrer Tochter … Ihrem Pächter … Ihrer Schwester … Ihrem Geschäftspart-ner … Ihrer Vorgesetzten … Ihrem Mitarbeiter … Ihrem Vater … Ihrer Vermieterin … Ihrem Freund …</p>

  <h2 class="stuck-question">SIE KOMMEN NICHT MEHR WEITER?</h2>
  <div class="grey-band"></div>
  <h2 class="mediation-title">MEDIATION</h2>
  <div class="mediation-text">
    <p>Die Konfliktparteien erarbeiten selber eine Lösung, begleitet und geführt durch eine Mediatorin.</p>
    <p>Ziel ist eine gemeinsam erarbeitete, stimmige, nachhaltige Lösung, die einen konstruktiven Umgang zwischen den Konfliktparteien wieder möglich macht.</p>
  </div>
  <div class="illustration" role="img" aria-label="Line drawing of three people standing together"></div>

  <p class="thesis-call">For my diploma thesis I am looking for conflicting parties who are willing to resolve their conflict with a mediator</p>
  <p class="time-frame"><strong>TIME FRAME:</strong>4 x 2.5 hours feasible in<br>Solothurn, Bern, Brugg</p>
  <p class="free-label">FREE OF CHARGE</p>

  <div class="brand-mark">
    <span class="dot"></span>
    <span class="name">Talweidenhof</span>
  </div>

  <svg class="footer" width="800" height="73" viewBox="0 0 800 73" aria-hidden="true">
    <polygon points="0,0 495,0 553,73 0,73" fill="#3e2454"/>
    <line x1="553" y1="62" x2="800" y2="62" stroke="#b8904a" stroke-width="3"/>
  </svg>
  <p class="footer-url">www.talweidenhof.ch</p>
</main>
</body>
</html>
```